Product label for KRAVO Athletic Fuel
KRAVO Athletic Fuel
Label required for protein powder supplement. Product manufactured in white cylindrical tub
Sports
Individuals involved with sports and fitness
The template should be completely redesigned, but the wording in the left and right columns should contain the same text. The centre column should contain editable wording as the template, with KRAVO logo and www.kravofuel.example web address
============Update=============
The label is 28cm x 14cm
Template
ai file for Logo
KRAVO Logo JPG

```html
<!DOCTYPE html>
<html lang="en">
<head>
<meta charset="utf-8">
<title>KRAVO Athletic Fuel – Whey 70 Label</title>
<link href="https://fonts.googleapis.com/css2?family=Anton&family=Roboto:wght@400;700;900&family=Roboto+Condensed:wght@700&display=swap" rel="stylesheet">
<style>
:root{
  --red:#d9252a;
  --deep-red:#a8191e;
  --yellow:#f4d31c;
  --ink:#1b1b1b;
  --grey:#6b6b6b;
  --rule:#c9c9c9;
  --paper:#ffffff;
  --panel:#f1f1f1;
}
*{box-sizing:border-box;margin:0;padding:0}
html,body{width:1200px;height:622px;overflow:hidden;background:var(--paper)}
body{font-family:"Roboto",Arial,sans-serif;color:var(--ink)}
.label{position:relative;width:1200px;height:622px;overflow:hidden;background:var(--paper)}

.top-band{position:absolute;left:0;top:0;width:1200px;height:54px;background:var(--red);color:#fff}
.product-code{position:absolute;left:18px;top:12px;font-family:"Anton",sans-serif;font-size:24px;letter-spacing:1px}
.facts-title{position:absolute;left:830px;top:15px;font-family:"Anton",sans-serif;font-size:21px;letter-spacing:1px}
.stats{position:absolute;left:440px;top:4px;display:flex;gap:26px}
.stat{text-align:center;line-height:1}
.stat-value{font-family:"Anton",sans-serif;font-size:24px;display:block}
.stat-name{font-family:"Roboto Condensed",sans-serif;font-size:9px;letter-spacing:1px;text-transform:uppercase;display:block;margin-top:3px}

.left-column{position:absolute;left:18px;top:64px;width:390px;font-size:8.4px;line-height:1.32;color:var(--ink)}
.left-column p{margin-bottom:7px}
.left-column .fine{font-size:6.8px;color:var(--grey);margin-bottom:5px}
.left-column strong{font-weight:700}

.food-band{position:absolute;left:0;bottom:0;width:420px;height:40px;background:var(--red);color:#fff;font-family:"Anton",sans-serif;font-size:19px;letter-spacing:1px;padding:8px 18px}

.centre-column{position:absolute;left:420px;top:54px;width:370px;height:568px;background:linear-gradient(180deg,var(--paper) 0%,var(--panel) 100%);border-left:1px solid var(--rule);border-right:1px solid var(--rule);text-align:center}
.brand{margin-top:38px;font-family:"Roboto",sans-serif;font-weight:900;font-size:62px;line-height:1;letter-spacing:2px;color:var(--ink)}
.brand-sub{font-weight:900;font-size:17px;letter-spacing:3px;color:var(--red);margin-top:6px}
.product-name{font-family:"Anton",sans-serif;line-height:.95;margin-top:22px}
.product-name .word-one{display:block;font-size:84px;color:var(--red)}
.product-name .word-two{display:block;font-size:66px;color:var(--deep-red)}
.product-desc{margin-top:14px;font-weight:900;font-size:11.5px;line-height:1.35;text-transform:uppercase;color:var(--ink)}
.flavour-band{margin:10px auto 0;width:250px;background:var(--yellow);font-family:"Roboto Condensed",sans-serif;font-size:15px;letter-spacing:1px;padding:3px 0;color:var(--ink)}
.net-weight{margin-top:10px;font-family:"Anton",sans-serif;font-size:17px;letter-spacing:1px;color:var(--ink)}
.web{margin-top:30px;font-weight:700;font-size:12px;letter-spacing:1px;color:var(--ink)}

.right-column{position:absolute;left:818px;top:66px;width:368px;font-size:9px;color:var(--ink)}
.serving{font-size:10px;line-height:1.4}
.facts-table{width:100%;border-collapse:collapse;margin-top:44px;font-size:9.4px}
.facts-table caption{text-align:right;font-size:8.5px;font-style:italic;padding-bottom:4px;color:var(--grey)}
.facts-table th{font-weight:700;text-align:right;padding:3px 2px;border-bottom:1.5px solid var(--ink)}
.facts-table th:first-child{text-align:left}
.facts-table td{padding:2.4px 2px;border-bottom:1px solid var(--rule);text-align:right}
.facts-table td:first-child{text-align:left}
.facts-table .strong td{font-weight:700}
.ingredients{margin-top:14px;font-size:9px;line-height:1.38}
.ingredients h3{font-size:9px;font-weight:700;margin-bottom:2px}
.maker{position:absolute;left:818px;top:552px;font-size:7.6px;line-height:1.3;font-weight:700;text-transform:uppercase}
</style>
</head>
<body>
<div class="label">

  <header class="top-band">
    <div class="product-code">WHEY 70</div>
    <div class="stats">
      <div class="stat"><span class="stat-value">37</span><span class="stat-name">Servings</span></div>
      <div class="stat"><span class="stat-value">230</span><span class="stat-name">Calories</span></div>
      <div class="stat"><span class="stat-value">21g</span><span class="stat-name">Carbs</span></div>
      <div class="stat"><span class="stat-value">30g</span><span class="stat-name">Protein</span></div>
      <div class="stat"><span class="stat-value">4.6g</span><span class="stat-name">Fat</span></div>
    </div>
    <div class="facts-title">SUPPLEMENT FACTS</div>
  </header>

  <section class="left-column">
    <p>Whey 70 is designed to transport maximum protein with rapid absorption. Whey contains high levels of BCAAs which are vital in the manufacture, maintenance and repair of muscle tissue.</p>
    <p>Whey 70 is rapidly absorbed, making the protein available for muscle building more quickly, and allowing the amino acids to be taken up by the muscles more quickly.</p>
    <p>In addition, whey assists in opening the bloodflow during exercise. The flow of nutrients to the muscles is increased, allowing a faster rate of muscle repair.</p>
    <p>Body builders and athletes will benefit from the high levels of BCAAs, their rapid absorption, and the premium-quality protein and carbohydrates contained in Whey 70.</p>
    <p>Whey 70 is an optimum blend of:<br><strong>- Instantized, De-lactosed Pure Whey Isolate</strong><br><strong>- Concentrate and Hydrolised Whey</strong></p>
    <p>This unique blend provides high levels of all Amino Acid fractions including L-Glutamine and BCAAs.</p>
    <p>SUGGESTED USE:<br>Mix one scoop (36g) with 300ml of water or milk</p>
    <p class="fine">ALLERGEN WARNING: This product is manufactured in a facility that also handles milk, soya, egg, nuts and gluten. Not suitable for anyone with these allergies.</p>
    <p class="fine">DISCLAIMER: This product is intended to support a varied diet and healthy lifestyle. It is not a medicine. Do not exceed the stated daily dose. Keep out of reach of children. Consult a doctor if pregnant or under medical care.</p>
    <p class="fine">BEST BEFORE: See base of container</p>
    <p class="fine">STORAGE: Store in a cool, dry place. Seal after opening.</p>
  </section>

  <div class="food-band">FOOD SUPPLEMENT</div>

  <section class="centre-column">
    <div class="brand">KRAVO</div>
    <div class="brand-sub">ATHLETIC FUEL</div>
    <h1 class="product-name"><span class="word-one">WHEY</span><span class="word-two">PROTEIN</span></h1>
    <p class="product-desc">Instantized Whey Isolate<br>Concentrate &amp; Hydrolysed Whey<br>Unique Blend of Amino Acids</p>
    <div class="flavour-band">BANANA FLAVOUR</div>
    <div class="net-weight">NET WEIGHT: 2.25 KG</div>
    <div class="web">www.kravofuel.example</div>
  </section>

  <section class="right-column">
    <p class="serving">SERVING SIZE: One level scoop 36g<br>Servings per container: 62</p>
    <table class="facts-table">
      <caption>Typical Analysis</caption>
      <thead><tr><th></th><th>Per serving</th><th>Per 100g</th></tr></thead>
      <tbody>
        <tr class="strong"><td>Kcals/serving</td><td>151</td><td>420</td></tr>
        <tr class="strong"><td>Protein (dry basis)</td><td>25.2g</td><td>70g</td></tr>
        <tr class="strong"><td>Fat (includes MCT Oil)</td><td>3.6g</td><td>10g</td></tr>
        <tr><td>of which saturates</td><td>0.7g</td><td>2g</td></tr>
        <tr><td>Trans Fat</td><td>0g</td><td>0g</td></tr>
        <tr class="strong"><td>Carbohydrates</td><td>6.4g</td><td>18g</td></tr>
        <tr><td>of which sugars</td><td>4g</td><td>11g</td></tr>
        <tr class="strong"><td>Sodium</td><td>Trace</td><td>Trace</td></tr>
        <tr class="strong"><td>Fibre</td><td>356mg</td><td>990mg</td></tr>
      </tbody>
    </table>
    <div class="ingredients">
      <h3>INGREDIENTS:</h3>
      <p>Instantised and Instantised Pure Whey Protein Concentrate, Pure Whey Protein Isolate, Hydrolised Whey Protein, Natural and Natural Identical Flavouring, Natural Colourings, Stabilisers (Citric acid, Malic acid), Sweetener: Sucralose.</p>
    </div>
  </section>

  <address class="maker">Manufactured in the UK for:<br>Brand<br>Address Line 1<br>Address Line 2<br>Postcode</address>

</div>
</body>
</html>
```